need a clean, modern job advertisement designed for social media (Facebook & Instagram).

The post is to advertise two positions:
• Leading Hand Boilermaker
• Dragline Fitter
We want the design to match our KRT Plant Services branding: blue, white, strong, professional, mining-industry style.
What the design should include:
Bold headline: “WE’RE HIRING”
Sub-headline: “Leading Hand Boilermaker & Dragline Fitter”
Key points:
• Bowen Basin based
• Dragline & shovel maintenance
• Great pay + long-term work
• Locally owned & operated
KRT logo placed cleanly
Space for 1–2 images (boilermaking or dragline work)
Design style:
Strong and industrial
Blue/white colour scheme
Easy to read at a glance
Suitable for a square 1080×1080 design

```html
<!DOCTYPE html>
<html lang="en">
<head>
<meta charset="utf-8">
<title>KRT Plant Services – We're Hiring</title>
<link rel="stylesheet" href="https://fonts.googleapis.com/css2?family=Anton&family=Barlow+Condensed:wght@500;600&display=swap">
<style>
  :root {
    --page-bg: #b3b3b3;
    --white: #ffffff;
    --ink: #0d0d0d;
    --blue-light: #35b2ff;
    --blue: #1b8cff;
    --blue-deep: #0a62e0;
    --navy: #0a2a66;
    --band-dark: #141414;
    --band-mid: #262626;
    --stripe-grey: #e6e6e6;
    --row-grey: #eeeeee;
  }
  * { margin: 0; padding: 0; box-sizing: border-box; }
  html, body { width: 1200px; height: 603px; overflow: hidden; }
  body { background: var(--page-bg); position: relative; }

  .stage { position: absolute; left: 320px; top: 21px; width: 560px; height: 560px; }
  .post {
    position: absolute; left: 0; top: 0;
    width: 1053px; height: 1053px;
    transform: scale(0.5318); transform-origin: 0 0;
    background: var(--white); overflow: hidden;
    font-family: "Barlow Condensed", "Arial Narrow", sans-serif;
  }
  .post-shapes { position: absolute; inset: 0; width: 1053px; height: 1053px; }

  .brand {
    position: absolute; left: 20px; top: 130px; width: 340px;
    display: flex; align-items: center; gap: 14px;
    font-weight: 600; font-size: 44px; line-height: 1; color: var(--blue-deep);
  }
  .brand-dot { width: 46px; height: 46px; border-radius: 50%; background: var(--blue-deep); flex: none; }

  .headline { position: absolute; right: 50px; top: 40px; text-align: right; font-family: "Anton", "Impact", sans-serif; line-height: 1; }
  .headline-top { display: block; font-size: 136px; color: var(--ink); letter-spacing: -2px; }
  .headline-main { display: block; font-size: 214px; color: var(--white); letter-spacing: -3px; margin-top: -26px; }

  .roles {
    position: absolute; left: 50px; top: 372px;
    font-weight: 600; font-size: 72px; line-height: 63px; color: var(--blue);
  }

  .points { position: absolute; left: 50px; top: 640px; list-style: none; }
  .points li {
    display: flex; align-items: center; gap: 14px;
    height: 68px; font-weight: 500; font-size: 54px; color: var(--ink);
  }
  .points li span { background: linear-gradient(90deg, var(--row-grey), rgba(238,238,238,0)); padding: 0 40px 0 6px; }
  .points svg { width: 34px; height: 34px; flex: none; }

  .contact {
    position: absolute; left: 50px; top: 956px; height: 50px;
    display: flex; align-items: center; gap: 12px;
    font-weight: 500; font-size: 34px; color: var(--navy);
  }
  .contact svg { width: 42px; height: 32px; flex: none; }
  .contact .phone-icon { width: 30px; height: 30px; margin-left: 20px; }
</style>
</head>
<body>
<div class="stage">
  <div class="post">
    <svg class="post-shapes" viewBox="0 0 1053 1053" aria-hidden="false">
      <defs>
        <linearGradient id="blueFade" x1="0" y1="0" x2="1" y2="0">
          <stop offset="0" stop-color="var(--blue-light)"/>
          <stop offset="1" stop-color="var(--blue-deep)"/>
        </linearGradient>
        <linearGradient id="bandFade" x1="0" y1="0" x2="1" y2="0">
          <stop offset="0" stop-color="var(--band-dark)"/>
          <stop offset="0.6" stop-color="var(--band-mid)"/>
          <stop offset="1" stop-color="var(--band-dark)"/>
        </linearGradient>
        <linearGradient id="weldTones" x1="0" y1="0" x2="1" y2="1">
          <stop offset="0" stop-color="#1a1410"/>
          <stop offset="0.35" stop-color="#c2461c"/>
          <stop offset="0.7" stop-color="#4a3f38"/>
          <stop offset="1" stop-color="#16120f"/>
        </linearGradient>
        <linearGradient id="mineTones" x1="0" y1="0" x2="0" y2="1">
          <stop offset="0" stop-color="#9cc6ea"/>
          <stop offset="0.5" stop-color="#dfe8ee"/>
          <stop offset="0.62" stop-color="#7a8c55"/>
          <stop offset="0.72" stop-color="#d9c49a"/>
          <stop offset="1" stop-color="#c9a771"/>
        </linearGradient>
        <linearGradient id="contactFade" x1="0" y1="0" x2="1" y2="0">
          <stop offset="0" stop-color="var(--blue)"/>
          <stop offset="1" stop-color="var(--blue-light)"/>
        </linearGradient>
      </defs>

      <!-- light diagonal accents -->
      <polygon points="330,0 372,0 262,190 220,190" fill="var(--stripe-grey)"/>
      <polygon points="395,0 455,0 345,190 285,190" fill="var(--stripe-grey)" opacity="0.7"/>

      <!-- headline panel -->
      <polygon points="505,0 1053,0 1053,455 530,455 375,225" fill="url(#blueFade)"/>
      <g fill="var(--white)">
        <polygon points="540,400 580,400 610,455 570,455"/>
        <polygon points="620,400 660,400 690,455 650,455"/>
        <polygon points="700,400 740,400 770,455 730,455"/>
        <polygon points="780,400 820,400 850,455 810,455"/>
        <polygon points="860,400 900,400 930,455 890,455"/>
        <polygon points="940,400 980,400 1010,455 970,455"/>
      </g>

      <!-- roles band -->
      <polygon points="0,358 428,358 560,592 0,592" fill="url(#bandFade)"/>

      <!-- image areas -->
      <polygon points="518,470 1053,470 1053,744 678,744" fill="url(#weldTones)" role="img" aria-label="Photo of a welder in orange workwear welding a large steel pipe with sparks flying"/>
      <polygon points="665,757 1053,757 1053,1053 525,1053" fill="url(#mineTones)" role="img" aria-label="Photo of a yellow dragline excavator working on a sandy open-cut mine site under a blue sky"/>

      <!-- contact bar -->
      <polygon points="0,954 565,954 545,1004 0,1004" fill="url(#contactFade)"/>
    </svg>

    <div class="brand"><span class="brand-dot"></span><span>KRT Plant Services</span></div>

    <h1 class="headline">
      <span class="headline-top">WE’RE</span>
      <span class="headline-main">HIRING</span>
    </h1>

    <h2 class="roles">Leading Hand<br>Boilermaker<br>&amp; Dragline Fitter</h2>

    <ul class="points">
      <li><svg viewBox="0 0 34 34"><path d="M4 4 L18 17 L4 30 L4 22 L10 17 L4 12 Z" fill="var(--blue-light)"/><path d="M14 4 L28 17 L14 30 L14 22 L20 17 L14 12 Z" fill="var(--blue-deep)"/></svg><span>Bowen Basin based</span></li>
      <li><svg viewBox="0 0 34 34"><path d="M4 4 L18 17 L4 30 L4 22 L10 17 L4 12 Z" fill="var(--blue-light)"/><path d="M14 4 L28 17 L14 30 L14 22 L20 17 L14 12 Z" fill="var(--blue-deep)"/></svg><span>Dragline &amp; shovel maintenance</span></li>
      <li><svg viewBox="0 0 34 34"><path d="M4 4 L18 17 L4 30 L4 22 L10 17 L4 12 Z" fill="var(--blue-light)"/><path d="M14 4 L28 17 L14 30 L14 22 L20 17 L14 12 Z" fill="var(--blue-deep)"/></svg><span>Great pay + long-term work</span></li>
      <li><svg viewBox="0 0 34 34"><path d="M4 4 L18 17 L4 30 L4 22 L10 17 L4 12 Z" fill="var(--blue-light)"/><path d="M14 4 L28 17 L14 30 L14 22 L20 17 L14 12 Z" fill="var(--blue-deep)"/></svg><span>Locally owned &amp; operated</span></li>
    </ul>

    <div class="contact">
      <svg viewBox="0 0 42 32"><rect x="2" y="2" width="38" height="28" fill="none" stroke="var(--white)" stroke-width="3"/><path d="M2 2 L21 18 L40 2 M2 30 L16 15 M40 30 L26 15" fill="none" stroke="var(--white)" stroke-width="3"/></svg>
      <span>admin@krtplant.com.au</span>
      <svg class="phone-icon" viewBox="0 0 24 24"><path d="M6.6 10.8a15.1 15.1 0 0 0 6.6 6.6l2.2-2.2c.3-.3.7-.4 1-.2 1.1.4 2.3.6 3.6.6.6 0 1 .4 1 1V20c0 .6-.4 1-1 1A17 17 0 0 1 3 4c0-.6.4-1 1-1h3.5c.6 0 1 .4 1 1 0 1.3.2 2.5.6 3.6.1.3 0 .7-.2 1z" fill="var(--white)"/></svg>
      <span>+61 400 318 572</span>
    </div>
  </div>
</div>
</body>
</html>
```